Medical Billing Business needs a web page designed

We need a web page for a new medical billing business for prospective clients to go to to get information about our company. It needs to show what our company stands for and our billing rates. Our colors are blue, gray and white. I have attached our logo, brochure and mission statement.

Need tabs at top for "about us", "contact us" "specials". On contact page, need a form to fill out that will be automatically emailed to us upon completion. Under specials...Sign a contract by the end of August 2014 and receive one month of billing FREE. ***Receive 25% off the first 4 months of the contract***

Medical

```html
<!DOCTYPE html>
<html lang="en">
<head>
<meta charset="utf-8">
<title>Northfield Medical Billing, LLC</title>
<link rel="stylesheet" href="https://fonts.googleapis.com/css2?family=Montserrat:wght@300;400;500;600;700&display=swap">
<style>
  :root {
    --navy: #06334d;
    --navy-deep: #052b42;
    --sky: #8fd3f2;
    --blue: #0d6795;
    --ink: #1c1c1c;
    --text-blue: #0b4a6e;
    --paper: #ffffff;
    --mist: #f4f4f4;
    --frame: #dcdcdc;
  }
  * { box-sizing: border-box; margin: 0; padding: 0; }
  html, body { width: 858px; height: 1200px; overflow: hidden; }
  body {
    position: relative;
    background: var(--paper);
    font-family: "Montserrat", Arial, sans-serif;
    color: var(--ink);
  }
  .abs { position: absolute; }

  .top-bar { left: 0; top: 0; width: 858px; height: 94px; background: var(--navy); }
  .phone { right: 90px; top: 10px; color: #e8f3f9; font-size: 15px; font-weight: 400; display: flex; align-items: center; gap: 10px; }

  .hero {
    left: 0; top: 94px; width: 858px; height: 399px;
    background: linear-gradient(90deg, #e3e8ee 0%, #c9d2dc 30%, #dfe7ee 55%, #eef2f6 80%, #e8edf2 100%);
  }
  .nav-band { left: 0; top: 94px; width: 858px; height: 56px; background: rgba(143, 211, 242, 0.85); }
  .nav a {
    position: absolute; top: 115px; font-size: 13px; font-weight: 600;
    color: var(--navy); text-decoration: none; letter-spacing: 0.3px;
  }
  .brand {
    left: 329px; top: 14px; width: 200px; text-align: center;
    color: #e8f3f9; font-weight: 500; font-size: 13px; line-height: 1.35; letter-spacing: 0.5px;
  }
  .brand-mark { display: block; width: 36px; height: 36px; margin: 0 auto 8px; border-radius: 50%; background: var(--blue); }
  .brand-name { color: var(--navy); }

  .hero-line { right: 90px; text-align: right; color: var(--text-blue); }
  .hero-line.small { top: 358px; font-size: 20px; font-weight: 400; }
  .hero-line.big { top: 380px; font-size: 27px; font-weight: 500; color: #0a3550; }
  .dots { right: 92px; top: 457px; display: flex; gap: 4px; }
  .dots span { width: 7px; height: 7px; border-radius: 50%; background: #fff; }
  .dots span.on { background: var(--navy); }

  .intro { left: 0; top: 493px; width: 858px; height: 222px; background: var(--mist); }
  .offer-box { left: 103px; top: 529px; width: 140px; height: 129px; }
  .offer-top { height: 93px; background: var(--blue); color: #fff; text-align: center; padding-top: 11px; font-weight: 700; line-height: 1; }
  .offer-top .q { font-size: 22px; }
  .offer-top .c { font-size: 27px; }
  .offer-top .s { font-size: 13px; line-height: 1.15; }
  .offer-bottom { height: 36px; background: var(--navy-deep); color: #fff; font-size: 11px; font-weight: 600; display: flex; align-items: center; justify-content: center; }

  .intro-title { left: 256px; top: 535px; font-size: 12.5px; font-weight: 700; color: var(--blue); letter-spacing: 0.3px; }
  .intro-copy { left: 256px; top: 561px; width: 480px; font-size: 9.4px; line-height: 17.2px; font-weight: 400; color: #222; }
  .tagline { left: 0; top: 681px; width: 858px; text-align: center; font-size: 12.5px; font-weight: 700; color: var(--navy); letter-spacing: 0.3px; }
  .tagline em { font-style: normal; color: var(--blue); }

  .card-media { top: 753px; width: 273px; height: 182px; border: 4px solid var(--frame); border-bottom-width: 5px; }
  .media-mission { left: 120px; background: linear-gradient(135deg, #eef3f6 0%, #dde7ec 50%, #c4ced6 100%); }
  .media-goals { left: 463px; background: linear-gradient(135deg, #3a3d42 0%, #5c6066 45%, #8a8d91 75%, #2b2e33 100%); }
  .card-title { top: 949px; font-size: 17.5px; font-weight: 500; color: #0a3550; }
  .card-copy { top: 992px; width: 280px; font-size: 9.6px; line-height: 17.2px; color: #222; }
  .card-copy b { font-weight: 600; color: #0a3550; }

  .footer { left: 0; top: 1137px; width: 858px; height: 63px; background: var(--navy); }
  .footer-links { left: 121px; top: 1151px; font-size: 10px; color: #e8f3f9; }
  .footer-links span { margin: 0 9px; }
  .copyright { left: 121px; top: 1174px; font-size: 10px; color: #e8f3f9; }
  .social { left: 740px; top: 1164px; display: flex; gap: 7px; }
  .social span { width: 9px; height: 9px; background: #e8f3f9; border-radius: 50%; }
</style>
</head>
<body>
  <div class="abs top-bar"></div>

  <div class="abs hero" role="img" aria-label="Photo of a smiling business man in a grey suit in front of a blurred medical team in white coats"></div>
  <div class="abs nav-band"></div>

  <div class="abs phone">
    <svg width="13" height="13" viewBox="0 0 13 13" aria-hidden="true">
      <rect width="13" height="13" rx="2" fill="#2f7fa8"/>
      <path d="M4 3.2c.4 0 1 1.2 1 1.6 0 .4-.6.6-.6 1 0 .7 1.2 1.9 1.9 1.9.4 0 .6-.6 1-.6s1.6.6 1.6 1c0 .8-.9 1.3-1.6 1.3C5.2 9.4 3.6 7.8 3.6 5.7c0-.7.4-2.5.4-2.5z" fill="#06334d"/>
    </svg>
    555-014-2290
  </div>

  <div class="abs brand">
    <span class="brand-mark"></span>
    <span class="brand-name">NORTHFIELD<br>Medical Billing, LLC</span>
  </div>

  <nav class="nav">
    <a href="#" style="left:163px">HOME</a>
    <a href="#" style="left:255px">ABOUT US</a>
    <a href="#" style="left:524px">CONTACT US</a>
    <a href="#" style="left:630px">SPECIALS</a>
  </nav>

  <div class="abs hero-line small">We are a medical billing</div>
  <div class="abs hero-line big">business company</div>
  <div class="abs dots"><span class="on"></span><span></span><span></span><span></span></div>

  <section class="abs intro"></section>
  <div class="abs offer-box">
    <div class="offer-top">
      <div class="q">QUICK</div>
      <div class="c">COST</div>
      <div class="s">EFFICIENT<br>SOLUTION</div>
    </div>
    <div class="offer-bottom">FOR YOUR PRACTICE</div>
  </div>
  <h2 class="abs intro-title">HIPAA COMPLIANT</h2>
  <p class="abs intro-copy">Lorem Ipsum is simply dummy text of the printing and typesetting industry. Lorem Ipsum has been the industry's standard dummy text ever since the 1500s, when an unknown printer took a galley of type and scrambled it to make a type specimen book. It has survived not only five centuries, but also the leap into electronic typesetting, remaining essentially unchanged.Sed ut perspiciatis unde omnis iste natus error sit voluptatem accusantium doloremque laudantium, totam rem aperiam, eaque ipsa quae ab illo inventore veritatis</p>
  <p class="abs tagline">ENHANCE &amp; IMPROVE <em>YOUR COLLECTION RATE</em></p>

  <div class="abs card-media media-mission" role="img" aria-label="Photo of two hands forming a framing gesture against a bright office"></div>
  <h3 class="abs card-title" style="left:121px">Our Mission</h3>
  <p class="abs card-copy" style="left:121px">Our mission at Northfield Medical Billing, LLC is to set the standard of excellence for providing quality medical ad-ministrative services to our clients. Our company's success, which is characterized by organizational excellence as well as our responsiveness.. <b>Read More</b></p>

  <div class="abs card-media media-goals" role="img" aria-label="Photo of a woman drawing a rising bar chart on glass"></div>
  <h3 class="abs card-title" style="left:463px">Goals</h3>
  <p class="abs card-copy" style="left:463px">We will stand firm to our Mission Statement by hiring only the most qualified employees who share our same vision and morals that will make us the premier and pre-ferred company &nbsp;.. <b>Read More</b></p>

  <footer class="abs footer"></footer>
  <div class="abs footer-links">Home<span>|</span>About Us<span>|</span>Contact Us<span>|</span>Specials</div>
  <div class="abs copyright">© 2014 Compnay Name,All Rights Reserved</div>
  <div class="abs social" aria-label="Social links"><span></span><span></span></div>
</body>
</html>
```